Lumbay! Laundry Detergent Powder Original Scent 500 grams

We need a packaging design for a new product- laundry detergent in powdered form. The first design will be the original scent and we will move on with the other variants once we have successfully launched this first one.

It will be in powdered form, no window on the packaging.

Target Market(s)

Men and Women ages 18-65 years old

Industry/Entity Type

Product

Font styles to use
Serif

Colors
9bcb3c
0255a3
f37122

Requirements
Must have
• Fresh and Clean look; Bright and solid colors (Please see photo attachment for an image guide of the look we are looking for)
• "Lumbay" is Filipino for Fresh, therefore the packaging must convey this.
• Packaging will be flexible bag in 500 gram pouch (3 side seal). Dimensions to follow.
• Product of China
• Net Weight: 500 grams as packed
• Other text to follow once your design is chosen
Nice to have
• Easy to read font on the brand name "Lumbay"
Should not have
• No black background colors

```html
<!DOCTYPE html>
<html lang="en">
<head>
<meta charset="utf-8">
<title>Lumbay Laundry Detergent – Original Scent Pouch Front</title>
<link rel="stylesheet" href="https://fonts.googleapis.com/css2?family=Open+Sans:wdth,wght@75..100,400..800&family=Quicksand:wght@500&display=swap">
<style>
  :root {
    --stage: #a9a8a8;
    --panel: #ffffff;
    --brand-blue: #0255a3;
    --brand-teal: #0b6b74;
    --brand-navy: #0a4a8c;
    --fresh-green: #9bcb3c;
    --lime: #cfe021;
    --leaf-green: #5cc02a;
    --sun-orange: #f37122;
    --amber: #f0961a;
    --ember: #f0501a;
    --sky: #3fb4e0;
    --white: #ffffff;
  }
  * { margin: 0; padding: 0; box-sizing: border-box; }
  html, body { width: 1200px; height: 1200px; overflow: hidden; }
  body {
    background: linear-gradient(160deg, #c3c1c1 0%, var(--stage) 60%, #9c9b9b 100%);
    position: relative;
    font-family: "Open Sans", sans-serif;
  }
  .pouch-front {
    position: absolute;
    left: 257px; top: 120px;
    width: 686px; height: 960px;
    background: var(--panel);
    overflow: hidden;
  }
  .fresh-artwork {
    position: absolute;
    left: 0; top: 0;
    width: 686px; height: 500px;
    background:
      radial-gradient(circle at 36% 4%, rgba(255,255,255,0.95) 0 3%, transparent 9%),
      radial-gradient(circle at 98% 16%, rgba(255,255,255,0.95) 0 3%, transparent 9%),
      radial-gradient(ellipse at 15% 20%, rgba(46,140,70,0.85) 0%, transparent 45%),
      radial-gradient(ellipse at 85% 15%, rgba(63,180,224,0.85) 0%, transparent 45%),
      radial-gradient(ellipse at 55% 40%, rgba(245,225,180,0.7) 0%, transparent 40%),
      radial-gradient(ellipse at 45% 30%, rgba(120,210,160,0.6) 0%, transparent 50%),
      linear-gradient(180deg, rgba(120,200,200,0.5) 0%, rgba(255,255,255,0) 100%);
  }
  .fresh-artwork::after {
    content: "";
    position: absolute; inset: 0;
    background: linear-gradient(180deg, transparent 45%, var(--panel) 100%);
  }
  .brand-block {
    position: absolute;
    left: 198px; top: 520px;
    width: 288px; height: 288px;
    background: linear-gradient(160deg, var(--brand-teal) 0%, #0f6f7c 35%, #0b5f96 65%, var(--brand-navy) 100%);
    color: var(--white);
    text-align: center;
  }
  .brand-name {
    position: absolute;
    left: 0; right: 0; top: 84px;
    font-size: 86px;
    font-weight: 700;
    font-stretch: 75%;
    line-height: 1;
    letter-spacing: 1px;
  }
  .product-type {
    position: absolute;
    left: 0; right: 0; top: 170px;
    font-family: "Quicksand", sans-serif;
    font-weight: 500;
    font-size: 23px;
  }
  .claim-tile {
    position: absolute;
    left: 547px;
    width: 139px; height: 139px;
    color: var(--white);
    font-weight: 700;
    font-stretch: 75%;
    padding-left: 17px;
  }
  .claim-tile--care {
    top: 522px;
    background: linear-gradient(120deg, var(--fresh-green) 0%, var(--leaf-green) 50%, var(--lime) 100%);
  }
  .claim-tile--size {
    top: 669px;
    background: linear-gradient(150deg, var(--amber) 0%, var(--sun-orange) 55%, var(--ember) 100%);
  }
  .care-line { position: absolute; left: 17px; font-size: 22px; line-height: 1.25; }
  .care-line--safe { top: 16px; }
  .care-line--machines { top: 70px; }
  .load-count { position: absolute; left: 16px; top: 6px; font-size: 54px; line-height: 1.1; }
  .load-count small { font-size: 24px; margin-left: 4px; }
  .net-weight { position: absolute; left: 16px; top: 96px; font-size: 22px; }
  .scent-name {
    position: absolute;
    left: 0; width: 686px; top: 858px;
    text-align: center;
    color: var(--brand-blue);
    font-size: 34px;
    font-weight: 700;
    font-stretch: 75%;
    padding-right: 2px;
    transform: translateX(-1px);
  }
  .scent-name span { display: inline-block; width: 686px; margin-left: -344px; }
</style>
</head>
<body>
  <main class="pouch-front">
    <div class="fresh-artwork" role="img" aria-label="Abstract illustration of translucent green, cream and sky-blue leaves and petals with light flares, fading to white"></div>

    <section class="brand-block">
      <h1 class="brand-name">LUMBAY</h1>
      <p class="product-type">laundry detergent</p>
    </section>

    <div class="claim-tile claim-tile--care">
      <p class="care-line care-line--safe">Color Safe</p>
      <p class="care-line care-line--machines">For all<br>Machines</p>
    </div>

    <div class="claim-tile claim-tile--size">
      <p class="load-count">48<small>loads</small></p>
      <p class="net-weight">500g</p>
    </div>

    <p class="scent-name" style="left:0;width:686px;transform:none;padding:0;left:-0px;margin-left:-86px;">Original Scent</p>
  </main>
</body>
</html>
```